Creative Web Design - Intl Market Research Company

We need an innovative web design for an emerging company into the international market research marketplace.

The company, Halvenor Associates, is a Trade, Investment, and Market Research company. Halvenor offers domestic and international companies increased success in the U.S. marketplace by providing a variety of services. (seen on attached brochure)

The website should be cutting edge and creative while having an easy navigation. The color is not fixed and attached logo is not finalized, feel free to post anything from conservative to progressive options. Keep in mind target customers are domestic and international businesses looking to emerge/improve in the U.S. marketplace.

Additional Company information is located in the attached documentation. The documentation is outdated & winner will have priority standing for our next projects.(logo & document re-design)

I have received a few e-mail requests and have updated the status to guaranteed payment.

Thanks!

Target Market(s)

Any company, foreign and domestic, looking to introduce their product into the U.S. marketplace.

Industry/Entity Type

Market Research

Requirements
Must have
• Easy Navigation
Should not have
• Too many buttons
Difficult navigation
Excessive Typography

```html
<!DOCTYPE html>
<html lang="en">
<head>
<meta charset="utf-8">
<title>Halvenor Associates</title>
<link href="https://fonts.googleapis.com/css2?family=Oswald:wght@300;400&family=Arimo:wght@400&display=swap" rel="stylesheet">
<style>
:root{
  --navy:#1d4a7c;
  --navy-dark:#17395f;
  --nav-top:#2f6399;
  --nav-bottom:#1f4b7d;
  --link:#1b5aa0;
  --lead:#183f78;
  --text:#666;
  --heading:#555;
  --rule:#e2e2e2;
  --btn:#2e2e2e;
  --footer:#ededed;
}
*{margin:0;padding:0;box-sizing:border-box}
html,body{width:1200px;height:1200px;overflow:hidden;background:#fff}
body{position:relative;font-family:"Arimo",Arial,sans-serif;color:var(--text)}
.abs{position:absolute}
.top-strip{left:0;top:0;width:1200px;height:4px;background:var(--navy-dark)}
.brand{left:120px;top:20px}
.brand-mark{width:40px;height:40px;border-radius:50%;background:var(--navy);margin-left:42px}
.brand-name{font-family:"Oswald",sans-serif;font-weight:400;font-size:25px;color:var(--navy);margin-top:12px;letter-spacing:-.3px;white-space:nowrap}
.region{left:949px;top:20px;width:132px;height:29px;border:1px solid #ddd;font-family:"Oswald",sans-serif;font-size:13px;color:#333;padding:5px 8px}
.region .sep{position:absolute;left:102px;top:5px;width:1px;height:18px;background:#ddd}
.region svg{position:absolute;left:110px;top:10px}
.search{left:869px;top:64px;width:212px;height:36px;border:1px solid #ddd;font-size:11px;color:#999;padding:10px 7px}
.search .sep{position:absolute;left:178px;top:0;width:1px;height:34px;background:#ddd}
.search svg{position:absolute;left:188px;top:9px}
.hero{left:0;top:139px;width:1200px;height:400px;background:linear-gradient(180deg,#3f7fc4 0%,#2a64a8 45%,#8ab9e2 100%)}
.nav{left:120px;top:116px;width:960px;height:45px;background:linear-gradient(180deg,var(--nav-top),var(--nav-bottom));display:flex;z-index:2}
.nav a{font-family:"Oswald",sans-serif;font-weight:400;font-size:18px;color:#fff;text-decoration:none;display:flex;align-items:center;justify-content:center;border-right:1px solid #1a3f69;height:45px}
.nav a:last-child{border-right:0}
.slider-dots{left:565px;top:513px;width:68px;height:26px;background:rgba(220,235,250,.55);border-radius:3px 3px 0 0;display:flex;gap:4px;justify-content:center;align-items:center}
.slider-dots span{width:12px;height:12px;border:2px solid #fff;border-radius:50%}
.slider-dots span.on{background:#fff}
.h2{font-family:"Oswald",sans-serif;font-weight:300;font-size:20px;color:var(--heading);letter-spacing:-.3px}
.h2 b{font-weight:400;color:var(--navy)}
.rule{height:1px;background:var(--rule)}
.photo{background:linear-gradient(135deg,#e8e4df,#c9b7a6 55%,#f2f2f2)}
.lead{font-size:13px;line-height:17px;color:var(--lead);text-align:justify}
.body{font-size:12px;line-height:17px;color:var(--text);text-align:justify}
.sources li{list-style:none;font-size:12px;color:var(--link);height:23px;padding-left:16px;position:relative}
.sources li::before{content:"";position:absolute;left:1px;top:3px;border-left:7px solid var(--navy-dark);border-top:4px solid transparent;border-bottom:4px solid transparent}
.arrow-btn{width:16px;height:16px;background:#777;border:1px solid #555}
.arrow-btn svg{display:block}
.svc-title{font-family:"Oswald",sans-serif;font-weight:400;font-size:16px;color:var(--navy);letter-spacing:-.3px}
.svc-img{width:220px;height:120px}
.more{width:62px;height:27px;background:var(--btn);color:#fff;font-family:"Oswald",sans-serif;font-size:12px;display:flex;align-items:center;justify-content:center}
.footer{left:0;top:1150px;width:1200px;height:50px;background:var(--footer)}
.copy{left:113px;top:1169px;font-size:12px;color:#444}
.social{left:900px;top:1165px;display:flex;gap:7px}
.social span{width:23px;height:23px;border-radius:4px}
</style>
</head>
<body>
<div class="abs top-strip"></div>

<header>
  <div class="abs brand">
    <div class="brand-mark"></div>
    <div class="brand-name">HALVENOR ASSOCIATES</div>
  </div>
  <div class="abs region">USA<span class="sep"></span>
    <svg width="12" height="8" viewBox="0 0 12 8"><path d="M0 0h12L6 8z" fill="#2a5d94"/></svg>
  </div>
  <div class="abs search">Search...<span class="sep"></span>
    <svg width="16" height="16" viewBox="0 0 16 16"><circle cx="6" cy="6" r="4" fill="none" stroke="#2a5d94" stroke-width="2"/><path d="M9 9l5 5" stroke="#2a5d94" stroke-width="2.5"/></svg>
  </div>
</header>

<div class="abs hero" role="img" aria-label="Blue-toned view looking up at modern glass office towers and construction cranes"></div>

<nav class="abs nav">
  <a style="width:95px">HOME</a>
  <a style="width:125px">ABOUT US</a>
  <a style="width:151px">OUR SERVICES</a>
  <a style="width:130px">SOLUTIONS</a>
  <a style="width:162px">NEWS &amp; EVENTS</a>
  <a style="width:156px">TESTIMONIALS</a>
  <a style="width:141px">CONTACT US</a>
</nav>
<div class="abs slider-dots"><span></span><span></span><span class="on"></span></div>

<section>
  <h2 class="abs h2" style="left:118px;top:553px">WELCOME TO <b>HALVENOR ASSOCIATES</b>!</h2>
  <div class="abs rule" style="left:118px;top:592px;width:631px"></div>
  <div class="abs photo" style="left:119px;top:611px;width:220px;height:178px" role="img" aria-label="Portrait of a smiling company representative"></div>
  <p class="abs lead" style="left:355px;top:608px;width:391px">At vero eos et accusamus et iusto odio dignissimos ducimus qui blanditiis praesentium voluptatum deleniti</p>
  <p class="abs body" style="left:355px;top:659px;width:391px">At vero eos et accusamus et iusto odio dignissimos ducimus qui blanditiis praesentium voluptatum deleniti Nam libero tempore, cum soluta nobis est eligendi optio cumque nihil impedit quo minus id quod maxime placeat facere possimus, omnis voluptas assumenda est, omnis dolor repellendus. Temporibus autem quibusdam et aut officiis debitis aut rerum necessitatibus saepe eveniet ut et voluptates repudiandae sint et molestiae non recusandae. Itaque earum rerum hic tenetur a sapiente delectus, ut aut reiciendis voluptatibus maiores</p>
</section>

<aside>
  <h2 class="abs h2" style="left:781px;top:553px">OUR SOURCES</h2>
  <div class="abs rule" style="left:779px;top:592px;width:300px"></div>
  <p class="abs body" style="left:779px;top:608px;width:300px;font-size:13px;line-height:16px">At vero eos et accusamus et iusto odio dignissimos ducimus qui blanditiis praesentium voluptatum deleniti</p>
  <ul class="abs sources" style="left:779px;top:664px">
    <li>Online Database</li>
    <li>CD ROM Database</li>
    <li>Industry Association</li>
    <li>Industry Experts</li>
    <li>Government Experts</li>
    <li>Government Agencies</li>
  </ul>
</aside>

<section>
  <div class="abs rule" style="left:118px;top:819px;width:961px"></div>
  <h2 class="abs h2" style="left:118px;top:835px">OUR SERVICES TO</h2>
  <div class="abs arrow-btn" style="left:1043px;top:836px"><svg width="14" height="14"><path d="M9 3L5 7l4 4" stroke="#fff" stroke-width="1.5" fill="none"/></svg></div>
  <div class="abs arrow-btn" style="left:1063px;top:836px"><svg width="14" height="14"><path d="M5 3l4 4-4 4" stroke="#fff" stroke-width="1.5" fill="none"/></svg></div>
  <div class="abs rule" style="left:118px;top:873px;width:961px"></div>

  <h3 class="abs svc-title" style="left:121px;top:886px">IMPORTERS</h3>
  <div class="abs svc-img" style="left:119px;top:915px;background:linear-gradient(135deg,#2a4f73,#0f2b48 60%,#3a6a90)" role="img" aria-label="Container ship at sea"></div>
  <p class="abs body" style="left:119px;top:1042px;width:220px">At vero eos et accusamus et iusto odio dignissimos ducimus qui blanditiis praesentium voluptatum deleniti</p>
  <div class="abs more" style="left:119px;top:1103px">READ MORE</div>

  <h3 class="abs svc-title" style="left:364px;top:886px">AGENTS/REPRESENTATIVES</h3>
  <div class="abs svc-img" style="left:365px;top:915px;background:linear-gradient(135deg,#e6e6e6,#8a8a8a 50%,#dcdcdc)" role="img" aria-label="Call centre agents wearing headsets"></div>
  <p class="abs body" style="left:365px;top:1042px;width:220px">At vero eos et accusamus et iusto odio dignissimos ducimus qui blanditiis praesentium voluptatum deleniti</p>
  <div class="abs more" style="left:365px;top:1103px">READ MORE</div>

  <h3 class="abs svc-title" style="left:611px;top:886px">DISTRIBUTORS</h3>
  <div class="abs svc-img" style="left:611px;top:915px;background:linear-gradient(135deg,#f2f2f2,#7a7f86 50%,#e8e8e8)" role="img" aria-label="Group of business people in suits"></div>
  <p class="abs body" style="left:611px;top:1042px;width:220px">At vero eos et accusamus et iusto odio dignissimos ducimus qui blanditiis praesentium voluptatum deleniti</p>
  <div class="abs more" style="left:611px;top:1103px">READ MORE</div>

  <h3 class="abs svc-title" style="left:856px;top:886px">MANUFACTURERS</h3>
  <div class="abs svc-img" style="left:857px;top:915px;background:linear-gradient(135deg,#9fd0f0,#2d78b8 50%,#c9e4f5)" role="img" aria-label="Factory floor with production machinery"></div>
  <p class="abs body" style="left:857px;top:1042px;width:220px">At vero eos et accusamus et iusto odio dignissimos ducimus qui blanditiis praesentium voluptatum deleniti</p>
  <div class="abs more" style="left:857px;top:1103px">READ MORE</div>
</section>

<footer>
  <div class="abs footer"></div>
  <p class="abs copy">©&nbsp; 2013 Halvenor Associates | All Rights Reserved.</p>
  <div class="abs social">
    <span style="background:#3a64b0"></span>
    <span style="background:#3aa6e0"></span>
    <span style="background:#1e7fc0"></span>
    <span style="background:#d8432f"></span>
    <span style="background:#d52b22"></span>
    <span style="background:#cc2028"></span>
  </div>
</footer>
</body>
</html>
```